Webdesign for Dutch IT consultancy company

Make a Wordpress webdesign for a Dutch consultancy company

Briefing Velmora IT

Website for finding and connecting IT-professionals. Corebusiness is to find IT-professionals and to help them to follow their ambitions. We offer training, personal coaching and education trajects.

U can take www.Tralvique.nl as an example for the website.

Home page

U can take www.Tralvique.nl as an example.

There should be jobs on the home page. A block for short info about us and about what whe do and a trigger to contact us quickly.

Jobs Page

On this page should be the jobs that we offer for the professionals. There should be a search function on this page so u can easily find the job that you are looking for.

A call to action can be on this page too.

Also a little block with text for some information.

For professionals page

Block with information on top. Call to action. info about who we work for/with.

For Clients

Info about three different solutions

- Sourcing solutions
- Consultancy solutions
- Custom based traineeships

Request a qoute option

Traineeships page

Info about two different traineeships

- Linux traineeships
- Microsoft traineeships

Call to action/ subscribe for traineeships

About us page

We are Velmora IT

Our mission: Creating cooperations between young professionals and businesses who wanna work on a great future.

Our core values

Last news

Target Market(s)

Young professionals and businesses who need IT services

Industry/Entity Type

It Company

Coding

Coded - Design and coding required

Number of Pages Required

5+ page

Font styles to use
Other font styles liked:
• Calibri

Colors
ffffff
add136
6b449b

Requirements
Must have
• Home page, Jobs Page, Professionals page, Clients page, Traineeships page, About us Page
• Green and/or Purple layout. Job search option, subscribe option
Nice to have
• modern design

```html
<!DOCTYPE html>
<html lang="en">
<head>
<meta charset="utf-8">
<title>Velmora IT – Sourcing | Consultancy</title>
<link href="https://fonts.googleapis.com/css2?family=Lato:ital,wght@0,400;0,700;0,900;1,400;1,700&family=Open+Sans:wght@400;600;700&display=swap" rel="stylesheet">
<style>
:root{
  --purple:#5b2f91;
  --purple-dark:#4a2479;
  --green:#9cc41f;
  --green-band:#a4cc32;
  --ink:#222;
  --text:#555;
  --line:#d9d9d9;
  --row-alt:#f4f4f4;
  --footer:#141414;
  --white:#fff;
}
*{margin:0;padding:0;box-sizing:border-box}
html,body{width:1200px;height:3226px;overflow:hidden}
body{font-family:"Open Sans",Arial,sans-serif;color:var(--text);background:var(--white);position:relative}
.container{position:absolute;left:99px;width:1002px}
a{text-decoration:none;color:inherit}

/* header */
.site-header{position:absolute;top:0;left:0;width:1200px;height:90px;background:var(--white)}
.brand{position:absolute;left:99px;top:22px}
.brand-name{font-family:"Lato",sans-serif;font-weight:900;font-size:32px;color:var(--purple);letter-spacing:1px;line-height:32px;text-transform:uppercase}
.brand-tag{font-size:8px;letter-spacing:2px;color:#777;margin-top:2px;padding-left:62px}
.main-nav{position:absolute;right:92px;top:34px;display:flex;gap:28px;font-family:"Lato",sans-serif;font-size:16px;color:#333}
.main-nav .active{color:var(--green)}
.search-icon{width:18px;height:18px}

/* hero */
.hero{position:absolute;top:90px;left:0;width:1200px;height:480px;background:linear-gradient(100deg,#d9dcdc 0%,#b9bcbb 40%,#7a7569 70%,#5d5a55 100%)}
.hero-title{position:absolute;left:99px;top:130px;width:560px;font-family:"Lato",sans-serif;font-weight:700;font-size:30px;line-height:44px;color:var(--white)}
.btn-solid{display:inline-block;background:var(--green);color:var(--white);font-family:"Lato",sans-serif;font-weight:700;font-size:16px;border-radius:24px;text-transform:uppercase}
.hero .btn-solid{position:absolute;left:99px;top:292px;width:155px;height:46px;line-height:46px;text-align:center}
.dots{position:absolute;left:567px;top:408px;display:flex;gap:4px}
.dots span{width:11px;height:11px;border-radius:50%;border:2px solid var(--white)}
.dots span.on{background:var(--white)}

/* welcome */
.welcome{top:570px;height:477px}
.section-title{font-family:"Lato",sans-serif;font-weight:900;font-size:32px;color:var(--ink);text-transform:uppercase}
.welcome .section-title{position:absolute;top:78px;left:0}
.welcome-text{position:absolute;top:134px;left:0;width:490px;font-size:13.5px;line-height:26px}
.welcome-text p+p{margin-top:24px}
.btn-outline{display:inline-block;border:2px solid #ccc;border-radius:22px;color:var(--green);font-family:"Lato",sans-serif;font-weight:700;font-size:15px;text-transform:uppercase;text-align:center}
.welcome .btn-outline{position:absolute;top:352px;left:0;width:126px;height:40px;line-height:36px}
.video-frame{position:absolute;left:535px;top:84px;width:467px;height:307px;border:1px solid var(--line);padding:8px;background:var(--white)}
.video-frame .media{width:100%;height:100%;background:linear-gradient(135deg,#e8ecee,#aab3b8 55%,#6f7275);position:relative}
.play{position:absolute;left:50%;top:50%;width:52px;height:52px;margin:-26px 0 0 -26px}

/* what we do */
.services{position:absolute;top:1047px;left:0;width:1200px;height:623px;background:linear-gradient(135deg,var(--purple) 0%,var(--purple-dark) 100%)}
.services .section-title{position:absolute;top:66px;width:1200px;text-align:center;color:var(--white)}
.service-card{position:absolute;top:140px;width:310px;height:404px;background:var(--white);border:3px solid var(--white);text-align:center}
.service-card .media{height:180px;background:linear-gradient(135deg,#dfe3e6,#9aa3aa)}
.service-card .badge{position:absolute;left:50%;top:150px;width:66px;height:66px;margin-left:-33px;border-radius:50%;background:var(--green);border:5px solid var(--white)}
.service-card .badge svg{width:100%;height:100%}
.service-card h3{margin-top:56px;font-family:"Lato",sans-serif;font-weight:900;font-size:21px;color:var(--ink);text-transform:uppercase}
.service-card p{margin:12px auto 0;width:250px;font-size:13.5px;line-height:24px}
.service-card .more{display:block;margin-top:12px;font-family:"Lato",sans-serif;font-weight:900;font-size:13.5px;color:var(--green);text-transform:uppercase}

/* jobs */
.jobs{top:1670px;height:919px}
.jobs .section-title{position:absolute;top:66px;width:100%;text-align:center}
.jobs-table{position:absolute;top:142px;left:0;width:1002px;border-collapse:collapse;border:1px solid var(--line)}
.jobs-table th{height:52px;background:var(--purple);color:var(--white);font-family:"Lato",sans-serif;font-weight:700;font-size:21px;border-right:1px solid #8f73b8}
.jobs-table td{height:125px;border:1px solid var(--line);vertical-align:middle;font-size:12.5px;line-height:23px}
.jobs-table tr:nth-child(even) td{background:var(--row-alt)}
.col-pos{width:284px;padding:0 30px;font-family:"Lato",sans-serif;font-weight:700;font-size:16px!important;color:var(--ink);line-height:26px!important}
.col-desc{width:344px;padding:0 16px}
.col-desc .more{color:var(--green);font-weight:700;font-size:12px}
.col-loc{width:219px;padding-left:24px;font-size:13px!important}
.col-loc svg{width:10px;height:13px;vertical-align:-2px;margin-right:6px}
.col-apply{text-align:center}
.col-apply .btn-outline{width:128px;height:36px;line-height:32px;font-size:14px;border-width:1.5px}

/* testimonial */
.testimonial{position:absolute;top:2589px;left:0;width:1200px;height:249px;background:linear-gradient(90deg,#9dc52a,var(--green-band) 50%,#9cc62c)}
.avatar{position:absolute;left:110px;top:62px;width:126px;height:126px;border-radius:50%;border:4px solid var(--white);background:linear-gradient(160deg,#e6e6e6,#9a9a9a)}
.testimonial .divider{position:absolute;left:268px;top:62px;width:2px;height:126px;background:rgba(255,255,255,.7)}
.quote{position:absolute;left:302px;top:60px;width:780px;font-family:"Lato",sans-serif;font-style:italic;font-size:15px;line-height:28px;color:var(--white)}
.quote cite{display:block;margin-top:14px;font-weight:700;font-size:20px}
.arrow{position:absolute;top:110px;width:20px;height:30px}

/* footer */
.site-footer{position:absolute;top:2838px;left:0;width:1200px;height:388px;background:var(--footer);color:#ddd}
.footer-brand{position:absolute;left:92px;top:148px}
.footer-brand .brand-name{color:var(--white);font-size:30px}
.footer-brand .brand-tag{color:#aaa}
.footer-col{position:absolute;top:74px}
.footer-col h4{font-family:"Lato",sans-serif;font-weight:700;font-size:16px;color:var(--white);text-transform:uppercase;margin-bottom:22px}
.quick-links{left:398px}
.quick-links li{list-style:none;font-size:12px;line-height:25px}
.newsletter{left:576px;width:260px}
.newsletter p{font-size:12px;line-height:22px}
.email-field{margin-top:18px;width:254px;height:36px;background:var(--white);color:#555;font-size:12px;padding:10px 12px}
.newsletter .btn-solid{margin-top:14px;width:108px;height:30px;line-height:30px;text-align:center;font-size:11px}
.contact{left:892px;width:230px}
.contact li{list-style:none;display:flex;gap:20px;font-size:12px;line-height:18px;margin-bottom:16px}
.contact svg{width:14px;height:14px;flex:none;margin-top:2px}
.footer-bottom{position:absolute;left:99px;top:305px;width:1002px;border-top:1px solid #333}
.copyright{position:absolute;left:0;top:30px;font-size:12px}
.social{position:absolute;right:0;top:18px;display:flex;gap:12px}
.social span{width:36px;height:36px;border-radius:50%;border:1.5px solid #ccc}
</style>
</head>
<body>

<header class="site-header">
  <div class="brand">
    <div class="brand-name">Velmora IT</div>
    <div class="brand-tag">SOURCING | CONSULTANCY</div>
  </div>
  <nav class="main-nav">
    <a class="active">Home</a><a>Jobs</a><a>Professionals</a><a>Clients</a><a>Traineeships</a><a>About us</a><a>Contact us</a>
    <svg class="search-icon" viewBox="0 0 20 20"><circle cx="8" cy="8" r="6" fill="none" stroke="#333" stroke-width="2.5"/><line x1="12.5" y1="12.5" x2="18" y2="18" stroke="#333" stroke-width="3"/></svg>
  </nav>
</header>

<section class="hero" role="img" aria-label="Photo of young professionals collaborating at a laptop in a bright office">
  <h1 class="hero-title">Creating cooperations between young professionals and businesses who wanna work on a great future</h1>
  <a class="btn-solid">Contact us</a>
  <div class="dots"><span class="on"></span><span></span><span></span><span></span></div>
</section>

<section class="container welcome">
  <h2 class="section-title">Welcome to Velmora IT</h2>
  <div class="welcome-text">
    <p>At vero eos et accusamus et iusto odio dignissimos ducimus qui blanditiis praesentium voluptatum deleniti atque.</p>
    <p>Corrupti quos dolores et quas molestias excepturi sint occaecati cupiditate non provident, similique sunt in culpa qui officia deserunt mollitia animi,id est laborum et dolorum fug harum quidem rerum facilis est et expeditdist incti m libero tempore, cum soluta nobi.</p>
  </div>
  <a class="btn-outline">Read more</a>
  <div class="video-frame">
    <div class="media" role="img" aria-label="Video still of a team meeting around a table with laptops">
      <svg class="play" viewBox="0 0 52 52"><circle cx="26" cy="26" r="24" fill="rgba(0,0,0,.55)" stroke="#fff" stroke-width="2.5"/><path d="M21 16 L36 26 L21 36Z" fill="#fff"/></svg>
    </div>
  </div>
</section>

<section class="services">
  <h2 class="section-title">What we do</h2>
  <article class="service-card" style="left:99px">
    <div class="media" role="img" aria-label="Photo of a trainer presenting to a group"></div>
    <div class="badge"><svg viewBox="0 0 56 56"><circle cx="24" cy="30" r="7" fill="none" stroke="#fff" stroke-width="4" stroke-dasharray="4 2.5"/><circle cx="24" cy="30" r="3" fill="#fff"/><circle cx="35" cy="21" r="4.5" fill="none" stroke="#fff" stroke-width="3" stroke-dasharray="3 2"/></svg></div>
    <h3>Training</h3>
    <p>Nam libero tempore, cum soluta nobis est eligendi optio cumque nihil impedit quo minus id quod maxime</p>
    <a class="more">Read more</a>
  </article>
  <article class="service-card" style="left:445px">
    <div class="media" role="img" aria-label="Photo of two men reviewing work on a laptop"></div>
    <div class="badge"><svg viewBox="0 0 56 56"><circle cx="28" cy="22" r="7" fill="#fff"/><path d="M15 40 Q15 30 28 30 Q41 30 41 40Z" fill="#fff"/></svg></div>
    <h3>Personal coaching</h3>
    <p>Nam libero tempore, cum soluta nobis est eligendi optio cumque nihil impedit quo minus id quod maxime</p>
    <a class="more">Read more</a>
  </article>
  <article class="service-card" style="left:791px">
    <div class="media" role="img" aria-label="Photo of a classroom with students at desks"></div>
    <div class="badge"><svg viewBox="0 0 56 56"><path d="M10 24 L28 16 L46 24 L28 32Z" fill="#fff"/><path d="M18 28 V36 Q28 42 38 36 V28 L28 33Z" fill="#fff"/><line x1="44" y1="25" x2="44" y2="36" stroke="#fff" stroke-width="2"/></svg></div>
    <h3>Education trajects</h3>
    <p>Nam libero tempore, cum soluta nobis est eligendi optio cumque nihil impedit quo minus id quod maxime</p>
    <a class="more">Read more</a>
  </article>
</section>

<section class="container jobs">
  <h2 class="section-title">Latest jobs</h2>
  <table class="jobs-table">
    <thead><tr><th>Positions</th><th>Description</th><th>Location</th><th></th></tr></thead>
    <tbody>
      <tr><td class="col-pos">At vero eos et accusamus et iusto odio dignissimo</td><td class="col-desc">Nemo enim ipsam voluptatem quia voluptas sit asp ernatur aut odit aut fugit, sed quia consequunt ma gni dolores eos qui ration.. <a class="more">READ MORE</a></td><td class="col-loc"><svg viewBox="0 0 10 13"><path d="M5 0 A4.5 4.5 0 0 1 9.5 4.5 C9.5 8 5 13 5 13 C5 13 .5 8 .5 4.5 A4.5 4.5 0 0 1 5 0Z" fill="#9cc41f"/><circle cx="5" cy="4.5" r="1.7" fill="#fff"/></svg>Elmira, Ontario, Canada</td><td class="col-apply"><a class="btn-outline">Apply now!</a></td></tr>
      <tr><td class="col-pos">At vero eos et accusamus et iusto odio dignissimo</td><td class="col-desc">Nemo enim ipsam voluptatem quia voluptas sit asp ernatur aut odit aut fugit, sed quia consequunt ma gni dolores eos qui ration.. <a class="more">READ MORE</a></td><td class="col-loc"><svg viewBox="0 0 10 13"><path d="M5 0 A4.5 4.5 0 0 1 9.5 4.5 C9.5 8 5 13 5 13 C5 13 .5 8 .5 4.5 A4.5 4.5 0 0 1 5 0Z" fill="#9cc41f"/><circle cx="5" cy="4.5" r="1.7" fill="#fff"/></svg>Hanover, Ontario, Canada</td><td class="col-apply"><a class="btn-outline">Apply now!</a></td></tr>
      <tr><td class="col-pos">At vero eos et accusamus et iusto odio dignissimo</td><td class="col-desc">Nemo enim ipsam voluptatem quia voluptas sit asp ernatur aut odit aut fugit, sed quia consequunt ma gni dolores eos qui ration.. <a class="more">READ MORE</a></td><td class="col-loc"><svg viewBox="0 0 10 13"><path d="M5 0 A4.5 4.5 0 0 1 9.5 4.5 C9.5 8 5 13 5 13 C5 13 .5 8 .5 4.5 A4.5 4.5 0 0 1 5 0Z" fill="#9cc41f"/><circle cx="5" cy="4.5" r="1.7" fill="#fff"/></svg>London, Ontario, Canada</td><td class="col-apply"><a class="btn-outline">Apply now!</a></td></tr>
      <tr><td class="col-pos">At vero eos et accusamus et iusto odio dignissimo</td><td class="col-desc">Nemo enim ipsam voluptatem quia voluptas sit asp ernatur aut odit aut fugit, sed quia consequunt ma gni dolores eos qui ration.. <a class="more">READ MORE</a></td><td class="col-loc"><svg viewBox="0 0 10 13"><path d="M5 0 A4.5 4.5 0 0 1 9.5 4.5 C9.5 8 5 13 5 13 C5 13 .5 8 .5 4.5 A4.5 4.5 0 0 1 5 0Z" fill="#9cc41f"/><circle cx="5" cy="4.5" r="1.7" fill="#fff"/></svg>Milton, Ontario, Canada</td><td class="col-apply"><a class="btn-outline">Apply now!</a></td></tr>
      <tr><td class="col-pos">At vero eos et accusamus et iusto odio dignissimo</td><td class="col-desc">Nemo enim ipsam voluptatem quia voluptas sit asp ernatur aut odit aut fugit, sed quia consequunt ma gni dolores eos qui ration.. <a class="more">READ MORE</a></td><td class="col-loc"><svg viewBox="0 0 10 13"><path d="M5 0 A4.5 4.5 0 0 1 9.5 4.5 C9.5 8 5 13 5 13 C5 13 .5 8 .5 4.5 A4.5 4.5 0 0 1 5 0Z" fill="#9cc41f"/><circle cx="5" cy="4.5" r="1.7" fill="#fff"/></svg>Mitchell, Ontario, Canada</td><td class="col-apply"><a class="btn-outline">Apply now!</a></td></tr>
    </tbody>
  </table>
</section>

<section class="testimonial">
  <svg class="arrow" style="left:36px" viewBox="0 0 20 30"><path d="M16 2 L4 15 L16 28" fill="none" stroke="rgba(255,255,255,.8)" stroke-width="2.5"/></svg>
  <div class="avatar" role="img" aria-label="Portrait photo of the client quoted"></div>
  <div class="divider"></div>
  <blockquote class="quote">
    Nam libero tempore, cum soluta nobis est eligendi optio cumque nihil impedit quo minus id quod maxime placeat facere possimus, omnis voluptas assumenda est, omnis dolor repellendus. Temporibus autem quibusdam et aut officiis debitis aut rerum necessitatibus saepe eveniet ut et voluptates repudiandae sint et molestiae
    <cite>- Marcel Dubreuil</cite>
  </blockquote>
  <svg class="arrow" style="right:36px" viewBox="0 0 20 30"><path d="M4 2 L16 15 L4 28" fill="none" stroke="rgba(255,255,255,.8)" stroke-width="2.5"/></svg>
</section>

<footer class="site-footer">
  <div class="footer-brand">
    <div class="brand-name">Velmora IT</div>
    <div class="brand-tag">SOURCING | CONSULTANCY</div>
  </div>
  <div class="footer-col quick-links">
    <h4>Quick links</h4>
    <ul><li>Help</li><li>FAQ</li><li>Support</li><li>Sitemap</li><li>Terms Of Use</li><li>Privacy Statement</li></ul>
  </div>
  <div class="footer-col newsletter">
    <h4>Newsletter subscription</h4>
    <p>Register your Email Address to get Information about us</p>
    <div class="email-field">Email Address</div>
    <a class="btn-solid">Subscribe</a>
  </div>
  <div class="footer-col contact">
    <h4>Contact us</h4>
    <ul>
      <li><svg viewBox="0 0 10 13"><path d="M5 0 A4.5 4.5 0 0 1 9.5 4.5 C9.5 8 5 13 5 13 C5 13 .5 8 .5 4.5 A4.5 4.5 0 0 1 5 0Z" fill="#fff"/><circle cx="5" cy="4.5" r="1.7" fill="#141414"/></svg><span>Unit 7 Harbour Lane<br>Greyfield Business Park</span></li>
      <li><svg viewBox="0 0 14 14"><path d="M3 1 L5.5 4 L4 6 Q6 9 8 10 L10 8.5 L13 11 L11 13.5 Q5 13 .5 3Z" fill="#fff"/></svg><span>1 555 010 2040</span></li>
      <li><svg viewBox="0 0 14 14"><rect x="1" y="4" width="12" height="9" fill="#fff"/><rect x="3" y="1" width="8" height="4" fill="none" stroke="#fff" stroke-width="1.5"/><rect x="3" y="7" width="8" height="2" fill="#141414"/></svg><span>1 555 010 3050</span></li>
      <li><svg viewBox="0 0 14 14"><rect x="0.5" y="2.5" width="13" height="9" fill="#fff"/><path d="M1 3 L7 8 L13 3" fill="none" stroke="#141414" stroke-width="1.2"/></svg><span>info@velmorait.com</span></li>
    </ul>
  </div>
  <div class="footer-bottom">
    <p class="copyright">Copyrights © 2017,&nbsp; Velmora IT&nbsp; All rights reserved.</p>
    <div class="social" aria-label="Social media links"><span></span><span></span><span></span></div>
  </div>
</footer>

</body>
</html>
```